new dating app design - young, fresh, clean

Project Brief

Zivvo is the world's first dating app that actually arranges dates. The process consists of 3 easy steps:

1. use our calendar to tell us when you'd like a date
2. browse singles nearby and select who you'd like to meet
3. when your date is 1 hour away, the app will find you a nice venue in the neighborhood and send one of your matches there to meet you. All you need to do is show up and have a good time.

This design assignment consists of creating a fun, fresh & user-friendly design for the wireframes created by our UX designer. Included are 2 screens:

1. the 'calendar' screen

2. the 'matches' screen

Also included is our style guide for your reference. Feel free to use as much or as little from this guide as you please. It would be nice if we could remain somewhat consistent with our previous design (which was purely based on this style guide) but we also want you to be creative and show off your skills so by no means should you feel obliged to conform to it.

Things to consider

1. 'calendar'

this is where you tell the app when you're free for a date. You can select as many time slots as you want. The info bars at the top and the bottom are 'sticky' (will stay in place no matter where in the screen you scroll to).

Everything about this page needs to be designed: not just in terms of spacing, font and coloring of the calendar itself but also the sticky bars at the bottom and top, and the interactions (when you select a time slot, what happens visually? How will it show that this slot was selected?).

TIP: please ignore the black vs white time slot distribution you see in the image. This was meant to signify where daytime becomes nighttime and vice versa, but we're not doing that anymore. So the only difference between blocks will be the difference between a selected and an unselected block. Make sure that difference is clearly visible in your design.

2. 'matches'

this is where you tell the app whom you'd like to meet with. You can select as many people as you want by clicking their 'heart' icon. You can scroll down to see more people and again the info bars at the top and/or bottom are sticky. The design elements for this page are:

a. the page itself (sizing, spacing of the images, etc.)
b. the interactions (how does a selected heart look, how does that compare to an unselected heart)

ICONS: feel free to come up with your own iconography (ie for the 'chat' icon in the top right, and/or the 'heart' icon signifying you want to meet this person. We really like the fact that the 'matches' and 'calendar' tabs are signified with words rather than icons, but feel free to get creative on this front as well. If you can make it prettier, we're all ears :) Whatever you do on this front, make sure all your icons and the rest of your work are/is free of copyright so we can actually use them in a commercially distributed app.

The winner of this contest may get awarded a follow-up project where they will be asked to design the entire app for us.

Reason: Thank you all for your submissions. We got some promising designs but nothing that was good enough just yet. We gave some feedback for improvement and wanted to give you guys some more time to get it right. New submissions are welcome too of course. Don't hesitate to contact us if you have any questions.

Target Market(s)

singles

Industry/Entity Type

Dating

Requirements
Must have
• fresh, clean, user-friendly design of the 2 pages provided. Your design choices should include decisions about font, sizing, colours, spacing, etc.
Nice to have
• custom icons, see project brief

```html
<!DOCTYPE html>
<html lang="en">
<head>
<meta charset="utf-8">
<title>Zivvo – Matches</title>
<link href="https://fonts.googleapis.com/css2?family=Lato:wght@400;700&display=swap" rel="stylesheet">
<style>
  :root {
    --header-top: #4b5286;
    --header-bottom: #5b6394;
    --header-text: #ffffff;
    --tab-active: #2d3470;
    --tab-inactive: #b9bccb;
    --tab-line: #f06d68;
    --tab-bg: #ffffff;
    --grid-bg: #eef0f3;
    --card-bg: #ffffff;
    --name: #2f376e;
    --heart-on: #f2545a;
    --heart-off: #e2e4e9;
    --footer-bg: #e6e8ee;
    --footer-text: #9da2b8;
    --badge: #f2545a;
  }
  * { box-sizing: border-box; margin: 0; padding: 0; }
  html, body { width: 681px; height: 1200px; overflow: hidden; }
  body {
    font-family: "Lato", "Helvetica Neue", Arial, sans-serif;
    background: var(--grid-bg);
    position: relative;
  }
  .app-header {
    position: absolute; left: 0; top: 0; width: 681px; height: 111px;
    background: linear-gradient(180deg, var(--header-top), var(--header-bottom));
    color: var(--header-text);
  }
  .status-bar {
    position: absolute; left: 0; top: 0; width: 100%; height: 40px;
    font-size: 19px; display: flex; align-items: center; padding: 0 20px;
  }
  .status-left { display: flex; align-items: center; gap: 6px; flex: 1; }
  .signal { display: flex; gap: 3px; }
  .signal span { width: 9px; height: 9px; border-radius: 50%; background: #fff; }
  .signal span.off { background: transparent; border: 1.5px solid #fff; }
  .status-time { flex: 1; text-align: center; font-weight: 700; }
  .status-right { flex: 1; display: flex; justify-content: flex-end; align-items: center; gap: 8px; }
  .battery { width: 40px; height: 16px; border: 1.5px solid #fff; border-radius: 3px; padding: 2px; position: relative; }
  .battery::after { content: ""; position: absolute; right: -5px; top: 4px; width: 3px; height: 6px; background: #fff; border-radius: 0 2px 2px 0; }
  .battery span { display: block; width: 100%; height: 100%; background: #fff; border-radius: 1px; }
  .nav-bar { position: absolute; left: 0; top: 40px; width: 100%; height: 71px; }
  .menu-icon { position: absolute; left: 52px; top: 26px; }
  .app-title {
    position: absolute; left: 0; right: 0; top: 20px; text-align: center;
    font-size: 29px; letter-spacing: 1px; font-weight: 400;
  }
  .chat-icon { position: absolute; left: 592px; top: 20px; }
  .chat-badge {
    position: absolute; left: 620px; top: 10px; width: 22px; height: 22px; border-radius: 50%;
    background: var(--badge); color: #fff; font-size: 13px; text-align: center; line-height: 22px;
  }
  .tabs {
    position: absolute; left: 0; top: 111px; width: 681px; height: 59px;
    background: var(--tab-bg); display: flex; border-bottom: 3px solid #e9eaef;
  }
  .tab {
    flex: 1; text-align: center; font-size: 19px; line-height: 56px; letter-spacing: 0.5px;
    color: var(--tab-inactive);
  }
  .tab.active { color: var(--tab-active); border-bottom: 4px solid var(--tab-line); margin-bottom: -3px; }
  .match-grid {
    position: absolute; left: 13px; top: 186px; width: 655px;
    display: grid; grid-template-columns: 321px 321px; column-gap: 13px; row-gap: 17px;
  }
  .match-card {
    background: var(--card-bg); height: 292px; border-radius: 4px; padding: 9px;
    box-shadow: 0 1px 3px rgba(60,70,110,0.08);
  }
  .match-photo { width: 303px; height: 216px; }
  .match-info { display: flex; align-items: center; justify-content: space-between; height: 58px; padding: 0 15px 0 20px; }
  .match-name { font-size: 21px; color: var(--name); letter-spacing: 0.3px; }
  .heart { width: 34px; height: 30px; }
  .heart.on path { fill: var(--heart-on); }
  .heart.off path { fill: var(--heart-off); }
  .photo-jessica { background: linear-gradient(135deg, #3f6a63, #c99a7c 55%, #6b5a55); }
  .photo-carry { background: linear-gradient(135deg, #f4f2f0, #b48a66 55%, #e5d6cd); }
  .photo-olivia { background: linear-gradient(135deg, #e7e4e0, #3a2a26 55%, #d9c2b6); }
  .photo-lesley { background: linear-gradient(135deg, #c7c3d9, #e685b3 55%, #b9b3cb); }
  .photo-natalie { background: linear-gradient(135deg, #d9d0c4, #6e4a3a 55%, #b5aeb0); }
  .photo-dylan { background: linear-gradient(135deg, #5b5652, #e2cfae 55%, #303030); }
  .info-footer {
    position: absolute; left: 0; top: 1120px; width: 681px; height: 80px; background: var(--footer-bg);
    color: var(--footer-text); font-size: 18px; text-align: center; line-height: 23px; padding-top: 16px; letter-spacing: 0.3px;
  }
  .info-footer svg { vertical-align: -3px; margin: 0 4px; }
</style>
</head>
<body>
  <header class="app-header">
    <div class="status-bar">
      <div class="status-left">
        <div class="signal"><span></span><span></span><span></span><span class="off"></span><span class="off"></span></div>
        <span>NOVA</span>
        <svg width="20" height="15" viewBox="0 0 20 15"><path d="M1 5a13 13 0 0 1 18 0M4 8a9 9 0 0 1 12 0M7 11a5 5 0 0 1 6 0" fill="none" stroke="#fff" stroke-width="2" stroke-linecap="round"/><circle cx="10" cy="13.5" r="1.5" fill="#fff"/></svg>
      </div>
      <div class="status-time">4:21 PM</div>
      <div class="status-right">
        <svg width="11" height="18" viewBox="0 0 11 18"><path d="M1 5l9 8-4.5 4V1L10 5 1 13" fill="none" stroke="#c9cce0" stroke-width="1.6"/></svg>
        <span>100%</span>
        <div class="battery"><span></span></div>
      </div>
    </div>
    <div class="nav-bar">
      <svg class="menu-icon" width="36" height="22" viewBox="0 0 36 22"><path d="M0 1h36M0 11h36M0 21h36" stroke="#fff" stroke-width="2"/></svg>
      <h1 class="app-title">Zivvo</h1>
      <svg class="chat-icon" width="40" height="38" viewBox="0 0 40 38"><path d="M20 3C10.6 3 3 9.6 3 17.7c0 4 1.8 7.6 4.8 10.2L6 35l8.2-3.7c1.8.5 3.8.8 5.8.8 9.4 0 17-6.6 17-14.4S29.4 3 20 3z" fill="none" stroke="#fff" stroke-width="2"/><circle cx="13" cy="18" r="1.6" fill="#fff"/><circle cx="20" cy="18" r="1.6" fill="#fff"/><circle cx="27" cy="18" r="1.6" fill="#fff"/></svg>
      <span class="chat-badge">3</span>
    </div>
  </header>

  <nav class="tabs">
    <div class="tab active">MATCHES</div>
    <div class="tab">SCHEDULE</div>
  </nav>

  <main class="match-grid">
    <article class="match-card">
      <div class="match-photo photo-jessica" role="img" aria-label="Profile photo of Jessica"></div>
      <div class="match-info"><span class="match-name">Jessica</span>
        <svg class="heart on" viewBox="0 0 34 30"><path d="M17 29S1 19 1 9.5A8.5 8.5 0 0 1 17 5a8.5 8.5 0 0 1 16 4.5C33 19 17 29 17 29z"/></svg></div>
    </article>
    <article class="match-card">
      <div class="match-photo photo-carry" role="img" aria-label="Profile photo of Carry"></div>
      <div class="match-info"><span class="match-name">Carry</span>
        <svg class="heart off" viewBox="0 0 34 30"><path d="M17 29S1 19 1 9.5A8.5 8.5 0 0 1 17 5a8.5 8.5 0 0 1 16 4.5C33 19 17 29 17 29z"/></svg></div>
    </article>
    <article class="match-card">
      <div class="match-photo photo-olivia" role="img" aria-label="Profile photo of Olivia"></div>
      <div class="match-info"><span class="match-name">Olivia</span>
        <svg class="heart off" viewBox="0 0 34 30"><path d="M17 29S1 19 1 9.5A8.5 8.5 0 0 1 17 5a8.5 8.5 0 0 1 16 4.5C33 19 17 29 17 29z"/></svg></div>
    </article>
    <article class="match-card">
      <div class="match-photo photo-lesley" role="img" aria-label="Profile photo of Lesley"></div>
      <div class="match-info"><span class="match-name">Lesley</span>
        <svg class="heart off" viewBox="0 0 34 30"><path d="M17 29S1 19 1 9.5A8.5 8.5 0 0 1 17 5a8.5 8.5 0 0 1 16 4.5C33 19 17 29 17 29z"/></svg></div>
    </article>
    <article class="match-card">
      <div class="match-photo photo-natalie" role="img" aria-label="Profile photo of Natalie"></div>
      <div class="match-info"><span class="match-name">Natalie</span>
        <svg class="heart off" viewBox="0 0 34 30"><path d="M17 29S1 19 1 9.5A8.5 8.5 0 0 1 17 5a8.5 8.5 0 0 1 16 4.5C33 19 17 29 17 29z"/></svg></div>
    </article>
    <article class="match-card">
      <div class="match-photo photo-dylan" role="img" aria-label="Profile photo of Dylan"></div>
      <div class="match-info"><span class="match-name">Dylan</span>
        <svg class="heart off" viewBox="0 0 34 30"><path d="M17 29S1 19 1 9.5A8.5 8.5 0 0 1 17 5a8.5 8.5 0 0 1 16 4.5C33 19 17 29 17 29z"/></svg></div>
    </article>
  </main>

  <footer class="info-footer">
    <p>Excellent! You can<svg width="22" height="19" viewBox="0 0 34 30"><path d="M17 29S1 19 1 9.5A8.5 8.5 0 0 1 17 5a8.5 8.5 0 0 1 16 4.5C33 19 17 29 17 29z" fill="#f2545a"/></svg>more if you’d like.</p>
    <p>Next, share your schedule and start dating!</p>
  </footer>
</body>
</html>
```